Food manufacturer stationary
Business cards, envelopes, letterhead, cover sheet etc
Professional
Gustavo Arrieta
CEO
2875 North Clover Ave Salt Lake City, UT 84117
GUSTAVOJR@CORVANAFOODS.EXAMPLE
WWW.CORVANAMEXICANFOODS.EXAMPLE
Looking for something classy, professional, and modern. Something that says to client holding card this is a well established strong company

```html
<!DOCTYPE html>
<html lang="en">
<head>
<meta charset="utf-8">
<title>Corvana Mexican Foods – Business Card</title>
<link rel="stylesheet" href="https://fonts.googleapis.com/css2?family=Tinos:ital,wght@0,400;1,400&display=swap">
<style>
  :root {
    --backdrop: #2a2a2c;
    --brown-light: #8a4d25;
    --brown-mid: #6b3618;
    --brown-dark: #421d0c;
    --gold: #e0b25a;
    --gold-deep: #a8742e;
    --cream: #f4e6cf;
    --white: #ffffff;
    --logo-brown: #5a2c12;
  }
  * { margin: 0; padding: 0; box-sizing: border-box; }
  html, body { width: 1200px; height: 1013px; overflow: hidden; }
  body {
    background: var(--backdrop);
    font-family: "Tinos", "Times New Roman", serif;
    position: relative;
  }
  .card {
    position: absolute;
    width: 687px;
    height: 387px;
    border-radius: 22px;
    overflow: hidden;
    box-shadow: 0 6px 18px rgba(0,0,0,.5);
  }
  .card--front { left: 96px; top: 102px; }
  .card--back {
    left: 404px; top: 527px;
    background: radial-gradient(ellipse at 50% 45%, var(--brown-light) 0%, var(--brown-mid) 50%, var(--brown-dark) 100%);
  }
  .card__shape { position: absolute; inset: 0; }

  .brand {
    position: absolute;
    display: flex;
    flex-direction: column;
    align-items: center;
    text-align: center;
  }
  .brand__dot {
    width: 64px; height: 64px;
    border-radius: 50%;
    background: var(--gold-deep);
    margin-bottom: 10px;
  }
  .brand__name {
    font-size: 46px;
    letter-spacing: 3px;
    line-height: 1;
  }
  .brand__tagline {
    font-size: 14px;
    font-style: italic;
    margin-top: 8px;
  }
  .card--front .brand { left: 22px; top: 92px; width: 230px; }
  .card--front .brand__name { color: var(--logo-brown); }
  .card--front .brand__tagline { color: var(--gold-deep); }
  .card--back .brand { left: 0; right: 0; top: 108px; }
  .card--back .brand__name { color: var(--gold); }
  .card--back .brand__tagline { color: var(--gold); }

  .holder {
    position: absolute;
    right: 44px; top: 20px;
    text-align: right;
  }
  .holder__name { color: var(--gold); font-size: 25px; }
  .holder__title { color: var(--cream); font-size: 15px; margin-top: 2px; }

  .contact {
    position: absolute;
    right: 22px; top: 236px;
    list-style: none;
    color: var(--cream);
    font-size: 14px;
    line-height: 22px;
  }
  .contact li {
    display: flex;
    justify-content: flex-end;
    align-items: center;
    gap: 8px;
  }
  .contact__icon { width: 14px; height: 14px; flex: none; }
  .contact__icon--blank { visibility: hidden; }
</style>
</head>
<body>

<section class="card card--front" aria-label="Business card front">
  <svg class="card__shape" viewBox="0 0 687 387" preserveAspectRatio="none" aria-hidden="true">
    <defs>
      <linearGradient id="panelBrown" x1="0" y1="0" x2="1" y2="1">
        <stop offset="0" stop-color="#8a4d25"/>
        <stop offset=".55" stop-color="#6b3618"/>
        <stop offset="1" stop-color="#421d0c"/>
      </linearGradient>
      <linearGradient id="bandGold" x1="0" y1="0" x2="0" y2="1">
        <stop offset="0" stop-color="#f3d48c"/>
        <stop offset=".5" stop-color="#c48d3e"/>
        <stop offset="1" stop-color="#8a5a22"/>
      </linearGradient>
    </defs>
    <rect width="687" height="387" fill="#ffffff"/>
    <path d="M300 0 C360 90 360 250 250 387 L687 387 L687 0 Z" fill="url(#bandGold)"/>
    <path d="M322 0 C382 95 378 255 272 387 L687 387 L687 0 Z" fill="url(#panelBrown)"/>
  </svg>

  <div class="brand">
    <span class="brand__dot"></span>
    <span class="brand__name">Corvana</span>
    <span class="brand__tagline">Mexican Foods, Inc</span>
  </div>

  <div class="holder">
    <p class="holder__name">Gustavo Arrieta</p>
    <p class="holder__title">CEO</p>
  </div>

  <ul class="contact">
    <li>2875 North Clover Ave
      <svg class="contact__icon" viewBox="0 0 14 14" aria-hidden="true"><path d="M7 1a4 4 0 0 0-4 4c0 3 4 8 4 8s4-5 4-8a4 4 0 0 0-4-4z" fill="#f4e6cf"/><circle cx="7" cy="5" r="1.5" fill="#6b3618"/></svg></li>
    <li>Salt Lake City, UT 84117
      <svg class="contact__icon contact__icon--blank" viewBox="0 0 14 14" aria-hidden="true"></svg></li>
    <li>801-555-0142
      <svg class="contact__icon" viewBox="0 0 14 14" aria-hidden="true"><rect x="3" y="2" width="8" height="10" rx="1.5" fill="none" stroke="#f4e6cf" stroke-width="1.5"/><rect x="5" y="4" width="4" height="4" fill="#f4e6cf"/></svg></li>
    <li>801-555-0187
      <svg class="contact__icon" viewBox="0 0 14 14" aria-hidden="true"><path d="M3 2h3l1 3-2 1a7 7 0 0 0 3 3l1-2 3 1v3a1 1 0 0 1-1 1A10 10 0 0 1 2 3a1 1 0 0 1 1-1z" fill="#f4e6cf"/></svg></li>
    <li>gustavojr@corvanafoods.example
      <svg class="contact__icon" viewBox="0 0 14 14" aria-hidden="true"><rect x="1.5" y="3" width="11" height="8" fill="none" stroke="#f4e6cf" stroke-width="1.3"/><path d="M1.5 3l5.5 4.5L12.5 3" fill="none" stroke="#f4e6cf" stroke-width="1.3"/></svg></li>
    <li>www.corvanamexicanfoods.example
      <svg class="contact__icon" viewBox="0 0 14 14" aria-hidden="true"><circle cx="7" cy="7" r="5.5" fill="none" stroke="#f4e6cf" stroke-width="1.3"/><path d="M1.5 7h11M7 1.5c-2.5 3-2.5 8 0 11M7 1.5c2.5 3 2.5 8 0 11" fill="none" stroke="#f4e6cf" stroke-width="1"/></svg></li>
  </ul>
</section>

<section class="card card--back" aria-label="Business card back">
  <div class="brand">
    <span class="brand__dot"></span>
    <span class="brand__name">Corvana</span>
    <span class="brand__tagline">Mexican Foods, Inc</span>
  </div>
</section>

</body>
</html>
```